Wine bottle labels - front and back - art and text provided

I have a logo (ai file) with our artwork, as well as all necessary text. I just need someone to put it all together and make it look neat, professional, and stylish, like a regular commercial wine bottle should be. This will be used for the front and back labels for our wine bottles for our very small home vineyard, not commercial use. I would like the style to be similar to the Copper Birch Sonoma Ridge brand with simple colors (grey and silver), and transparent so they can be screen-printed. I need both ai and jpg files. Note: There need to be two versions of each label. One with the date on the front and the ALC percentage on the back to see the complete look. The second version, without these items. This is because we are having all bottles screen printed without this information since we have a very small production, and will be adding small stickers WITH the information during bottling so that we can use the same bottles for years to come. Art file is attached. Front label text in addition to art: Cabernet Sauvignon 55% / Merlot 45% 2018 California. The back label should read: FERNHOLLOW ESTATE Nestled in the heart of the “Amber Crescent” in Quail Meadow, CA, the vineyard at Fernhollow Estate enjoys a year-round growing season. Nourished by the fertile black clay soil, the vineyard is surrounded by lush French lavender, fragrant roses, numerous fruit trees, and grazing horses. The Whitcombe family has been tending the vineyard at Fernhollow Estate since 2014. Our blend of 55% Cabernet Sauvignon and 45% Merlot results in a wine that is deep, vibrant, complex, and full of life. Enjoy our wine responsibly. Salut! Produced and bottled by Fernhollow Estate, Larkspur Bend, Westvale. GOVERNMENT WARNING: (1) ACCORDING TO THE SURGEON GENERAL, WOMEN SHOULD NOT DRINK ALCOHOLIC BEVERAGES DURING PREGNANCY BECAUSE OF THE RISK OF BIRTH DEFECTS. (2) CONSUMPTION OF ALCOHOLIC BEVERAGES IMPAIRS YOUR ABILITY TO DRIVE A CAR OR OPERATE MACHINERY, AND MAY CAUSE HEALTH PROBLEMS. CONTAINS SULFITES / 13.9% ALC BY VOL / 750 ML ***Font can be no smaller than 2mm tall, and items in bold must be the entire Government Warning and the "55% Cabernet Sauvignon / 45% Merlot".

Font styles to use
Serif
Script

Colors
cbcbcb

Requirements
Must have
• Transparent image in grey and silver so that the black bottle will show through the image as a background color.
Nice to have
• It would be nice to see the outline of the artwork in silver and everything else in grey. (see sample file of "Copper Birch" below.)

```html
<!DOCTYPE html>
<html lang="en">
<head>
<meta charset="utf-8">
<title>Fernhollow Estate – Front and Back Labels</title>
<link rel="stylesheet" href="https://fonts.googleapis.com/css2?family=Tinos:ital,wght@0,400;0,700;1,400;1,700&display=swap">
<style>
  :root {
    --bottle: #1c1c1f;
    --grey: #cbcbcb;
    --silver: #e6e6e8;
  }
  * { box-sizing: border-box; margin: 0; padding: 0; }
  html, body {
    width: 1197px;
    height: 1200px;
    overflow: hidden;
    background: var(--bottle);
  }
  body {
    position: relative;
    font-family: "Tinos", "Times New Roman", serif;
    color: var(--grey);
  }
  .label {
    position: absolute;
    top: 300px;
  }
  .label-frame {
    position: absolute;
    inset: 0;
    width: 100%;
    height: 100%;
  }
  .label-frame path {
    fill: none;
    stroke: var(--silver);
  }
  .label-frame .frame-outer { stroke-width: 3; }
  .label-frame .frame-inner { stroke-width: 1.5; }

  /* Front label */
  .front-label {
    left: 70px;
    width: 460px;
    text-align: center;
  }
  .front-plate {
    position: relative;
    height: 250px;
    display: flex;
    flex-direction: column;
    align-items: center;
    justify-content: center;
  }
  .brand-name {
    position: relative;
    font-size: 32px;
    font-weight: 400;
    letter-spacing: 2px;
    white-space: nowrap;
    color: var(--silver);
  }
  .brand-est {
    position: relative;
    margin-top: 14px;
    font-size: 17px;
    color: var(--grey);
    display: flex;
    align-items: center;
    gap: 10px;
  }
  .brand-est::before,
  .brand-est::after {
    content: "";
    width: 40px;
    height: 1px;
    background: var(--grey);
  }
  .varietals {
    margin-top: 30px;
    font-style: italic;
    font-weight: 700;
    font-size: 22px;
    line-height: 1.3;
  }
  .vintage {
    margin-top: 26px;
    font-weight: 700;
    font-size: 18px;
  }

  /* Back label */
  .back-label {
    left: 640px;
    width: 490px;
    height: 470px;
  }
  .back-copy {
    position: relative;
    padding: 28px 34px 0;
    font-size: 14.5px;
    line-height: 1.42;
  }
  .back-title {
    text-align: center;
    font-weight: 700;
    font-size: 15px;
    letter-spacing: 1px;
    margin-bottom: 8px;
  }
  .story {
    font-style: italic;
    text-align: justify;
    text-align-last: center;
  }
  .story strong { font-weight: 700; }
  .sign-off {
    font-style: italic;
    text-align: center;
    margin-top: 10px;
  }
  .producer {
    text-align: center;
    margin-top: 10px;
  }
  .warning {
    margin-top: 12px;
    font-weight: 700;
    font-size: 12.5px;
    line-height: 1.35;
    text-align: justify;
  }
  .warning-title,
  .sulfites { text-align: center; }
  .alc-volume {
    position: absolute;
    left: 0;
    right: 0;
    top: 484px;
    text-align: center;
    font-weight: 700;
    font-size: 13px;
  }
</style>
</head>
<body>

  <section class="label front-label" aria-label="Front label">
    <div class="front-plate">
      <svg class="label-frame" viewBox="0 0 460 250" preserveAspectRatio="none" aria-hidden="true">
        <path class="frame-outer" d="M24 4 H436 A20 20 0 0 0 456 24 V226 A20 20 0 0 0 436 246 H24 A20 20 0 0 0 4 226 V24 A20 20 0 0 0 24 4 Z"/>
        <path class="frame-inner" d="M28 12 H432 A16 16 0 0 0 448 28 V222 A16 16 0 0 0 432 238 H28 A16 16 0 0 0 12 222 V28 A16 16 0 0 0 28 12 Z"/>
      </svg>
      <h1 class="brand-name">FERNHOLLOW ESTATE</h1>
      <p class="brand-est">Est. 2014</p>
    </div>
    <p class="varietals">Cabernet Sauvignon 55%<br>Merlot 45%</p>
    <p class="vintage">2018</p>
  </section>

  <section class="label back-label" aria-label="Back label">
    <svg class="label-frame" viewBox="0 0 490 470" preserveAspectRatio="none" aria-hidden="true">
      <path class="frame-outer" d="M24 4 H466 A20 20 0 0 0 486 24 V446 A20 20 0 0 0 466 466 H24 A20 20 0 0 0 4 446 V24 A20 20 0 0 0 24 4 Z"/>
      <path class="frame-inner" d="M28 12 H462 A16 16 0 0 0 478 28 V442 A16 16 0 0 0 462 458 H28 A16 16 0 0 0 12 442 V28 A16 16 0 0 0 28 12 Z"/>
    </svg>
    <div class="back-copy">
      <h2 class="back-title">FERNHOLLOW ESTATE</h2>
      <p class="story">Nestled in the heart of the “Amber Crescent” in Quail Meadow, CA, the vineyard at Fernhollow Estate enjoys a year-round growing season. Nourished by the fertile black clay soil, the vineyard is surrounded by lush French lavender, fragrant roses, numerous fruit trees, and grazing horses. The Whitcombe family has been tending the vineyard at Fernhollow Estate since 2014. Our blend of <strong>55% Cabernet Sauvignon and 45% Merlot</strong> results in a wine that is deep, vibrant, complex, and full of life.</p>
      <p class="sign-off">Enjoy our wine responsibly. SALUT!</p>
      <p class="producer">Produced and bottled by<br>Fernhollow Estate, Larkspur Bend, Westvale.</p>
      <div class="warning">
        <p class="warning-title">GOVERNMENT WARNING:</p>
        <p>(1) ACCORDING TO THE SURGEON GENERAL, WOMEN SHOULD NOT DRINK ALCOHOLIC BEVERAGES DURING PREGNANCY BECAUSE OF THE RISK OF BIRTH DEFECTS. (2) CONSUMPTION OF ALCOHOLIC BEVERAGES IMPAIRS YOUR ABILITY TO DRIVE A CAR OR OPERATE MACHINERY, AND MAY CAUSE HEALTH PROBLEMS.</p>
        <p class="sulfites">CONTAINS SULFITES</p>
      </div>
    </div>
    <p class="alc-volume">13.9% ALC BY VOL / 750 ML.</p>
  </section>

</body>
</html>
```